Ranked amongst the Best Colleges and Programs

the size of the ad is Full Page, with bleed*
8”x 10.75" plus 0.25" bleed'
you have two choices for the tagline .. please chose what ever you think will allow you to make a better ad.
The instructions on the brief are in red
I am looking for a hight quality modern ad to place in local weekly publications that will stand out .
I would like a ad that people will look at and say i would like to see what this ad is all about.
I apprecate creative work.
the ad should not be very crowded and the text should be able to be read.
if you decide to use people in the ad .. (you don't have to ) then it should be a male dressed in white shirt in and sports jacket.. or if you would like you can use a vector and then use male or female people.
please leave one inch on the bottom for the footer

Target Market(s)

potential middle class students from 23-35 years of age

Industry/Entity Type

education

Requirements
Must have
• .the " 98% employment rate" should stand out in the ad.. but should not be the main part of the ad
Nice to have
• creative
Should not have
• Should not be a very busy or crowded ad.. i prefer pictures of men but should be .. in a business suit .. that looks professional- white shirt

```html
<!DOCTYPE html>
<html lang="en">
<head>
<meta charset="utf-8">
<title>NCU Masters of Accounting – Full Page Ad</title>
<link rel="stylesheet" href="https://fonts.googleapis.com/css2?family=Jost:wght@300;400&family=League+Spartan:wght@700;800&family=Montserrat:wght@800&display=swap">
<style>
  :root {
    --ink: #0d0d0d;
    --panel: #1a1a1a;
    --paper: #ffffff;
    --chip: #e6e6e6;
    --icon-fill: #8c8c8c;
    --icon-ring: #bdbdbd;
    --rule: #d9d9d9;
    --office-light: #f2f2f2;
    --office-mid: #bdbdbd;
    --office-dark: #2e2e2e;
  }
  * { box-sizing: border-box; margin: 0; padding: 0; }
  html, body { width: 960px; height: 1200px; overflow: hidden; background: var(--paper); }
  .ad { position: relative; width: 960px; height: 1200px; overflow: hidden; font-family: "Jost", sans-serif; color: var(--ink); }

  /* Hero photo area: tonal placeholder of a bright office scene */
  .hero-photo {
    position: absolute; left: 0; top: 0; width: 960px; height: 629px; overflow: hidden;
    background: linear-gradient(90deg, #e4e4e4 0%, #d6d6d6 30%, #c8c8c8 50%, #a9a9a9 70%, #8a8a8a 100%);
  }
  .hero-photo .tone { position: absolute; filter: blur(18px); }
  .tone-window-a { left: 40px;  top: -40px; width: 120px; height: 520px; background: var(--office-light); }
  .tone-window-b { left: 250px; top: -40px; width: 90px;  height: 500px; background: #f7f7f7; }
  .tone-column-a { left: 450px; top: -40px; width: 22px;  height: 560px; background: #9a9a9a; filter: blur(6px) !important; }
  .tone-column-b { left: 520px; top: -40px; width: 36px;  height: 560px; background: #7c7c7c; filter: blur(8px) !important; }
  .tone-window-c { left: 580px; top: -40px; width: 130px; height: 380px; background: #ececec; }
  .tone-figure {
    left: 520px; top: 120px; width: 520px; height: 560px; border-radius: 45% 40% 0 0;
    background: radial-gradient(ellipse at 60% 45%, #262626 0%, #3a3a3a 45%, #5a5a5a 80%);
    filter: blur(28px) !important;
  }
  .tone-desk {
    left: -40px; top: 540px; width: 1040px; height: 140px;
    background: linear-gradient(180deg, #f4f4f4, #e2e2e2);
    filter: blur(10px) !important;
  }

  .headline { position: absolute; left: 0; top: 0; width: 520px; height: 520px; }
  .headline .line { position: absolute; left: 79px; white-space: nowrap; line-height: 1; }
  .light { font-family: "Jost", sans-serif; font-weight: 300; }
  .heavy { font-family: "League Spartan", sans-serif; font-weight: 800; }
  .article { font-size: 52px; margin-right: 10px; }
  .line-small { top: 92px; }
  .line-small .heavy { font-size: 82px; letter-spacing: -2px; }
  .line-investment { top: 169px; font-size: 60px; letter-spacing: -1.5px; }
  .line-today { top: 219px; font-size: 62px; letter-spacing: -1px; }
  .line-big { top: 284px; }
  .line-big .heavy { font-size: 104px; letter-spacing: -2px; }
  .line-difference { top: 381px; font-size: 60px; letter-spacing: -1.5px; }
  .line-tomorrow { top: 435px; font-size: 64px; letter-spacing: 0; }

  .info-panel { position: absolute; left: 0; top: 629px; width: 960px; height: 571px; background: var(--panel); color: var(--paper); }

  .program-chip {
    position: absolute; left: 77px; top: 53px; width: 330px; height: 67px;
    background: var(--chip); border-radius: 12px;
    display: flex; align-items: center; gap: 16px; padding-left: 26px; color: #2a2a2a;
  }
  .program-name { font-family: "League Spartan", sans-serif; font-weight: 800; font-size: 50px; letter-spacing: -1px; line-height: 1; padding-top: 6px; }
  .program-title { font-weight: 300; font-size: 22px; line-height: 0.9; letter-spacing: 0.5px; text-transform: uppercase; }

  .stat-divider { position: absolute; left: 469px; top: 53px; width: 2px; height: 67px; background: var(--rule); }
  .employment-stat { position: absolute; left: 514px; top: 60px; display: flex; align-items: center; gap: 20px; }
  .stat-value { font-family: "League Spartan", sans-serif; font-weight: 800; font-size: 56px; letter-spacing: -2px; line-height: 1; padding-top: 6px; }
  .stat-label { font-weight: 300; font-size: 25px; line-height: 0.92; letter-spacing: 4px; text-transform: uppercase; }

  .rankings { position: absolute; left: 88px; top: 153px; width: 260px; }
  .rank-head { display: flex; align-items: flex-end; gap: 12px; }
  .rank-head p { font-weight: 300; font-size: 17px; line-height: 1; text-transform: uppercase; }
  .rank-item { margin-top: 22px; font-size: 22px; line-height: 1.12; }
  .rank-item strong { font-family: "Montserrat", sans-serif; font-weight: 800; display: block; }
  .rank-item span { font-weight: 300; }
  .rank-item + .rank-item { margin-top: 28px; }

  .column-rule { position: absolute; left: 355px; top: 177px; width: 2px; height: 215px; background: var(--rule); }

  .outcome-icon { position: absolute; left: 415px; }
  .icon-one { top: 172px; }
  .icon-two { top: 298px; }
  .outcome-text { position: absolute; left: 558px; width: 340px; font-weight: 300; font-size: 20px; line-height: 1.1; }
  .text-one { top: 180px; }
  .text-two { top: 306px; }

  .footer-frame {
    position: absolute; left: 94px; top: 466px; width: 773px; height: 120px;
    border: 1px solid var(--rule); border-bottom: none; border-radius: 36px 36px 0 0;
  }
</style>
</head>
<body>
<main class="ad">
  <div class="hero-photo" role="img" aria-label="Black and white photo of a professional man in a suit and white shirt thinking at a laptop in a bright office">
    <div class="tone tone-window-a" aria-hidden="true"></div>
    <div class="tone tone-window-b" aria-hidden="true"></div>
    <div class="tone tone-column-a" aria-hidden="true"></div>
    <div class="tone tone-column-b" aria-hidden="true"></div>
    <div class="tone tone-window-c" aria-hidden="true"></div>
    <div class="tone tone-figure" aria-hidden="true"></div>
    <div class="tone tone-desk" aria-hidden="true"></div>
  </div>

  <h1 class="headline">
    <span class="line line-small"><span class="light article">A</span><span class="heavy">SMALL</span></span>
    <span class="line line-investment heavy">INVESTMENT</span>
    <span class="line line-today light">TODAY</span>
    <span class="line line-big"><span class="light article">A</span><span class="heavy">BIG</span></span>
    <span class="line line-difference heavy">DIFFERENCE</span>
    <span class="line line-tomorrow light">TOMORROW</span>
  </h1>

  <section class="info-panel">
    <div class="program-chip">
      <span class="program-name">NCU</span>
      <span class="program-title">Masters of<br>Accounting</span>
    </div>

    <div class="stat-divider"></div>
    <div class="employment-stat">
      <span class="stat-value">98%</span>
      <span class="stat-label">Employment<br>Rate</span>
    </div>

    <div class="rankings">
      <div class="rank-head">
        <svg width="64" height="62" viewBox="0 0 64 62" fill="none" stroke="#fff" stroke-width="2">
          <path d="M22 2 l2.4 5 5.4 .6 -4 3.7 1.1 5.3 -4.9-2.7 -4.9 2.7 1.1-5.3 -4-3.7 5.4-.6z" stroke-width="1.6"/>
          <rect x="4" y="38" width="9" height="16"/>
          <rect x="18" y="22" width="9" height="32"/>
          <rect x="32" y="34" width="9" height="20"/>
          <rect x="46" y="28" width="9" height="26"/>
          <line x1="0" y1="58" x2="60" y2="58"/>
        </svg>
        <p>Ranked<br>Amongst</p>
      </div>
      <div class="rank-item"><strong>Best Colleges</strong><span>Ledger Review 2023</span></div>
      <div class="rank-item"><strong>Best Masters in Accounting</strong><span>Campus Rankings 2023</span></div>
    </div>

    <div class="column-rule"></div>

    <svg class="outcome-icon icon-one" width="96" height="100" viewBox="0 0 96 100">
      <path d="M4 48 A44 44 0 0 1 92 48" fill="none" stroke="var(--icon-ring)" stroke-width="3"/>
      <circle cx="48" cy="54" r="44" fill="var(--icon-fill)"/>
      <circle cx="46" cy="34" r="6" fill="var(--panel)"/>
      <circle cx="44" cy="57" r="13" fill="none" stroke="var(--panel)" stroke-width="4"/>
      <line x1="53" y1="66" x2="64" y2="77" stroke="var(--panel)" stroke-width="5" stroke-linecap="round"/>
    </svg>
    <p class="outcome-text text-one">NCU Graduates have gone<br>on to Work in Various<br>High-quality Jobs in Top Firms</p>

    <svg class="outcome-icon icon-two" width="96" height="100" viewBox="0 0 96 100">
      <path d="M4 48 A44 44 0 0 1 92 48" fill="none" stroke="var(--icon-ring)" stroke-width="3"/>
      <circle cx="48" cy="54" r="44" fill="var(--icon-fill)"/>
      <circle cx="52" cy="36" r="10" fill="none" stroke="var(--panel)" stroke-width="2.5"/>
      <text x="52" y="41" font-family="Jost, sans-serif" font-size="14" text-anchor="middle" fill="var(--panel)">$</text>
      <path d="M22 66 l10-10 h14 l4 4 h-12 M38 60 h14 l12-10 l4 4 -16 16 h-18 l-6 6" fill="none" stroke="var(--panel)" stroke-width="2.5" stroke-linejoin="round"/>
    </svg>
    <p class="outcome-text text-two">Earning Impressive Six-figure<br>Salaries as Well as Opening<br>Successful Businesses.</p>

    <div class="footer-frame"></div>
  </section>
</main>
</body>
</html>
```